Re-design of veterinary clinic website *

For a future relaunch of our webpage, we would like to find a fresh design that still incorporates the spirit of our current one which can be found at http://dr-wenzlaff.de
We are a small business that appeals to locals but are known in a wide area for specialist services.
According to analytics data, most people rarely read through the full website but are using it to inform themselves about opening hours, Telephone numbers and location. Still, the website needs to offer enough content to be ranked positively by the Quandle algorithm.
Our logo is not part of the re-design but needs to be included in your proposal as is. It can be used a source of inspiration, just as the current design. Keep in mind, that the design will be used as the basis of a fluid webdesign for both mobile and desktop. Roughly 75% of our users are on mobile devices.
Target Market(s)
Locals
Industry/Entity Type
Veterinary
Number of Pages Required
1 page
Look and feel
Each slider illustrates characteristics of the customer's brand and the style your logo design should communicate.

```html
<!DOCTYPE html>
<html lang="de">
<head>
<meta charset="utf-8">
<title>Tierarztpraxis Jonas Feldmann</title>
<link href="https://fonts.googleapis.com/css2?family=Quicksand:wght@400;500;600;700&display=swap" rel="stylesheet">
<style>
:root{
  --navy:#1f2d6b;
  --hero-a:#22347f;
  --hero-b:#5f74e0;
  --ink:#2f3f95;
  --accent:#6a82e6;
  --muted:#8a8fa3;
  --line:#c9ccd6;
  --white:#ffffff;
}
*{margin:0;padding:0;box-sizing:border-box}
html,body{width:722px;height:1200px;overflow:hidden;background:var(--white)}
body{font-family:'Quicksand',sans-serif;color:var(--ink);position:relative}
.abs{position:absolute}
.site-header{left:0;top:0;width:722px;height:61px;background:var(--navy)}
.brand{left:0;width:722px;top:21px;display:flex;justify-content:center;align-items:center;gap:8px;color:var(--white);font-weight:600;font-size:13px;letter-spacing:3px}
.brand-dot{width:14px;height:14px;border:1.5px solid var(--white);border-radius:50%}
.main-nav{left:0;top:61px;width:722px;height:25px;display:flex;justify-content:center;align-items:center;gap:13px;font-size:6px;font-weight:700;letter-spacing:.5px}
.hero{left:0;top:86px;width:722px;height:277px;background:linear-gradient(90deg,var(--hero-a) 0%,#2c3f95 45%,var(--hero-b) 100%)}
.hero-photo{left:360px;top:0;width:362px;height:277px;background:radial-gradient(ellipse at 60% 55%,#8d9ff0 0%,#6b80e2 40%,rgba(60,80,180,0) 75%)}
.hero-title{left:160px;width:200px;top:74px;text-align:center;color:var(--white);font-weight:400;font-size:21px;letter-spacing:2px;line-height:26px}
.hero-sub{left:150px;width:220px;top:136px;text-align:center;color:var(--white);font-weight:700;font-size:9px;letter-spacing:1.2px;line-height:16px}
.hero-down{left:352px;top:240px}
.hours-photo{left:160px;top:400px;width:150px;height:162px;border-radius:40px 40px 10px 10px;background:radial-gradient(ellipse at 50% 55%,#8b7b68 0%,#a8998a 45%,rgba(255,255,255,0) 72%)}
.hours-title{right:192px;top:401px;font-size:15px;font-weight:500}
.hours-note{right:192px;top:425px;font-size:9px;color:var(--muted);font-weight:500}
.hours-rule{left:549px;top:403px}
.hours-table{left:370px;top:455px;border-collapse:collapse;font-size:7px}
.hours-table td{height:18px;padding:0}
.hours-table .day{width:61px;font-weight:600;color:var(--ink)}
.hours-table .time{width:59px;color:#333;font-weight:500}
.contact{left:0;top:606px;width:361px;height:217px;background:var(--navy)}
.contact-rule{left:0;top:40px}
.contact-title{left:194px;top:38px;color:var(--white);font-size:15px;font-weight:500}
.contact-sub{left:194px;top:62px;color:#9aa0b8;font-size:9px;font-weight:500}
.contact-addr{left:195px;top:87px;color:var(--white);font-size:6.5px;line-height:9px;font-weight:500}
.contact-list{left:194px;top:122px;list-style:none;color:var(--white);font-size:8px;font-weight:600;letter-spacing:.3px}
.contact-list li{display:flex;align-items:center;gap:13px;height:22px}
.map{left:362px;top:606px;width:360px;height:217px;background:linear-gradient(135deg,#dcdcdc,#e6e3da 55%,#d8dcd6)}
.info-title{left:0;width:722px;top:860px;text-align:center;font-size:14px;font-weight:500}
.info-text{left:241px;width:240px;top:891px;text-align:center;font-size:6.5px;line-height:8.5px;font-weight:500}
.info-track{left:0;top:930px}
.info-label{width:110px;text-align:center;font-size:7px;font-weight:700;letter-spacing:1.4px}
.info-note{width:110px;text-align:center;font-size:6px;line-height:8px;font-weight:500}
.site-footer{left:0;top:1080px;width:722px;height:120px;background:var(--navy);color:var(--white);text-align:center}
.footer-name{left:0;width:722px;top:35px;font-size:7px;font-weight:700;letter-spacing:1.6px}
.social{left:0;width:722px;top:55px;display:flex;justify-content:center;gap:14px}
.social span{width:9px;height:9px;border-radius:50%;background:var(--white)}
.copyright{left:0;width:722px;top:80px;font-size:6.5px;font-weight:500}
</style>
</head>
<body>
<header class="abs site-header">
  <div class="abs brand"><span>Jonas Feldmann</span><span class="brand-dot"></span></div>
</header>
<nav class="abs main-nav">
  <span>HAUPTSEITE</span><span>PRAXIS</span><span>TEAM</span><span>SPRECHZEITEN</span><span>LEISTUNGEN</span><span>KONTAKT / ANFAHRT</span>
</nav>

<section class="abs hero">
  <div class="abs hero-photo" role="img" aria-label="Foto einer langhaarigen Katze in Blau getönt"></div>
  <h1 class="abs hero-title">HERZLICH<br>WILLKOMMEN!</h1>
  <p class="abs hero-sub">AUF DER HOMEPAGE DER<br>TIERARZTPRAXIS VON<br>DR. JONAS FELDMANN.</p>
  <svg class="abs hero-down" width="19" height="19" viewBox="0 0 19 19"><circle cx="9.5" cy="9.5" r="8.5" fill="none" stroke="#fff" stroke-width="1.3"/><path d="M6 8l3.5 3.5L13 8" fill="none" stroke="#fff" stroke-width="1.5"/></svg>
</section>

<div class="abs hours-photo" role="img" aria-label="Foto eines liegenden Hundes mit Wecker"></div>
<h2 class="abs hours-title">Sprechzeiten</h2>
<p class="abs hours-note">ohne Terminvereinbarung</p>
<svg class="abs hours-rule" width="173" height="16"><circle cx="8" cy="8" r="7" fill="#fff" stroke="var(--line)" stroke-width="1.3"/><line x1="15" y1="8" x2="173" y2="8" stroke="var(--line)" stroke-width="1"/></svg>
<table class="abs hours-table">
  <tr><td class="day">Montag</td><td class="time">9.30 - 11.00</td><td class="time">16.00 - 19.00</td></tr>
  <tr><td class="day">Dienstag</td><td class="time">9.30 - 11.00</td><td class="time">16.00 - 19.00</td></tr>
  <tr><td class="day">Mittwoch</td><td class="time">9.30 - 11.00</td><td class="time">16.00 - 19.00</td></tr>
  <tr><td class="day">Donnerstag</td><td class="time"></td><td class="time">16.00 - 19.00</td></tr>
  <tr><td class="day">Freitag</td><td class="time">9.30 - 11.00</td><td class="time">16.00 - 19.00</td></tr>
  <tr><td class="day">Samstag</td><td class="time">9.30 - 11.00</td><td class="time"></td></tr>
</table>

<section class="abs contact">
  <svg class="abs contact-rule" width="172" height="16"><line x1="0" y1="8" x2="155" y2="8" stroke="var(--line)" stroke-width="1"/><circle cx="162" cy="8" r="7" fill="var(--navy)" stroke="var(--line)" stroke-width="1.3"/></svg>
  <h2 class="abs contact-title">Kontakt</h2>
  <p class="abs contact-sub">Dr. med. vet. Jonas Feldmann</p>
  <p class="abs contact-addr">Fachtierarzt für Kleintiere<br>Lindenweg 4b</p>
  <ul class="abs contact-list">
    <li><svg width="9" height="12" viewBox="0 0 9 12"><path d="M4.5 11.3S.7 7 .7 4.5a3.8 3.8 0 0 1 7.6 0C8.3 7 4.5 11.3 4.5 11.3z" fill="none" stroke="#fff"/><circle cx="4.5" cy="4.5" r="1.3" fill="none" stroke="#fff"/></svg>10115 Musterstadt (Nordviertel)</li>
    <li><svg width="9" height="12" viewBox="0 0 9 12"><rect x="1" y=".6" width="7" height="10.8" rx="1" fill="none" stroke="#fff"/><line x1="3.5" y1="9.5" x2="5.5" y2="9.5" stroke="#fff"/></svg>030 / 555 12 34</li>
    <li><svg width="9" height="12" viewBox="0 0 9 12"><path d="M.7.6h5l2.6 2.6v8.2H.7z" fill="none" stroke="#fff"/></svg>030 / 555 12 35</li>
  </ul>
</section>
<div class="abs map" role="img" aria-label="Stadtplan mit Standort der Tierarztpraxis Dr. Feldmann"></div>

<h2 class="abs info-title">Weitere informationen</h2>
<p class="abs info-text">Lorem ipsum dolor sit amet, consectetur adipisicing elit, sed do eiusmod tempor incididunt ut labore et dolore magna aliqua. Ut enim ad minim veniam, quis nostrud exercitation ullamco.</p>
<svg class="abs info-track" width="722" height="76" viewBox="0 0 722 76">
  <line x1="173" y1="37" x2="722" y2="37" stroke="var(--line)" stroke-width="1"/>
  <circle cx="166" cy="37" r="7" fill="#fff" stroke="var(--line)" stroke-width="1.3"/>
  <g fill="#fff" stroke="var(--accent)" stroke-width="1.4">
    <circle cx="251" cy="37" r="30"/><circle cx="361" cy="37" r="30"/><circle cx="471" cy="37" r="30"/>
  </g>
  <g fill="var(--ink)">
    <rect x="241" y="24" width="20" height="26"/>
    <g fill="#fff"><rect x="245" y="28" width="3" height="3"/><rect x="254" y="28" width="3" height="3"/><rect x="245" y="34" width="3" height="3"/><rect x="254" y="34" width="3" height="3"/><rect x="249" y="42" width="4" height="8"/></g>
    <circle cx="354" cy="31" r="5"/><circle cx="369" cy="32" r="4.5"/>
    <path d="M344 47c0-7 4-9 10-9s10 2 10 9z"/><path d="M361 47c0-6 3-8 8-8s8 2 8 8z"/>
    <path d="M463 22h16l-4 9h-8z"/><circle cx="471" cy="40" r="9"/>
    <path fill="#fff" d="M471 34.5l1.6 3.4 3.7.4-2.8 2.5.8 3.6-3.3-1.9-3.3 1.9.8-3.6-2.8-2.5 3.7-.4z"/>
  </g>
</svg>
<div class="abs info-label" style="left:196px;top:1012px">PRAXIS</div>
<div class="abs info-label" style="left:306px;top:1010px">TEAM</div>
<div class="abs info-label" style="left:416px;top:1010px">LEISTUNGEN</div>
<p class="abs info-note" style="left:196px;top:1024px">Lorem ipsum dolor sit amet, consectetur.</p>
<p class="abs info-note" style="left:306px;top:1022px">Lorem ipsum dolor sit amet, consectetur.</p>
<p class="abs info-note" style="left:416px;top:1022px">Lorem ipsum dolor sit amet, consectetur.</p>

<footer class="abs site-footer">
  <div class="abs footer-name">JONAS FELDMANN - TIERARZTPRAXIS</div>
  <div class="abs social" aria-label="Soziale Netzwerke"><span></span><span></span><span></span><span></span></div>
  <div class="abs copyright">© 2019 JONAS FELDMANN Alle Rechte Vorbehalten</div>
</footer>
</body>
</html>
```